bluegum voyages

We provide boar charter for :Fishing/whale watching and diving in Sydney Harbour providing for 12 passengersI have yet to have web page made but want to make logo first then do web page later. So I want to be able to edit and add this site to card later

Contact Information for Business Card

Captain Art (Doc) Wigellphone no 0457710098email awigell4@gmail.comCompany name Marlow Outings Pty Ltd in association with far reef cruises

Font styles to use
Serif

Requirements
Nice to have
• perhaps a photo of boat and some stick diagrams of fishing.whales and diviving

```html
<!DOCTYPE html>
<html lang="en">
<head>
<meta charset="utf-8">
<title>Marlow Outings Pty Ltd – Business Card</title>
<link href="https://fonts.googleapis.com/css2?family=Noto+Serif:wght@400;700&display=swap" rel="stylesheet">
<style>
  :root {
    --navy: #234295;
    --white: #ffffff;
    --backdrop: #efe7d8;
    --photo-sky: #f1f2f4;
    --photo-hull: #e4e8ee;
    --photo-deck: #b9c3cf;
    --photo-water: #2f4a46;
  }
  * { margin: 0; padding: 0; box-sizing: border-box; }
  html, body {
    width: 1189px; height: 1200px; overflow: hidden;
    background: var(--backdrop);
    font-family: "Noto Serif", Georgia, serif;
  }
  .card {
    position: absolute; left: 171px; width: 856px; height: 488px;
    background: var(--white);
  }
  .card--front { top: 66px; }
  .card--back { top: 626px; }
  .card__rule {
    position: absolute; top: 0; left: 406px; width: 3px; height: 100%;
    background: var(--navy);
  }
  .card__panel {
    position: absolute; top: 0; left: 412px; right: 0; height: 100%;
    background: var(--navy); color: var(--white);
  }
  .card__photo {
    position: absolute; top: 0; left: 0; width: 406px; height: 100%;
    background: linear-gradient(180deg,
      var(--photo-sky) 0%, var(--photo-sky) 30%,
      var(--photo-deck) 42%, var(--photo-hull) 55%,
      var(--photo-hull) 76%, var(--photo-water) 90%, var(--photo-water) 100%);
  }
  .brand {
    position: absolute; width: 320px; text-align: center;
  }
  .brand--light { color: var(--navy); left: 43px; top: 290px; }
  .brand--dark { color: var(--white); left: 62px; top: 284px; }
  .brand__name {
    font-size: 27px; line-height: 34px; font-weight: 400; letter-spacing: 0.5px;
  }
  .brand__legal {
    display: flex; align-items: center; justify-content: center; gap: 10px;
    font-size: 19px; line-height: 22px; font-weight: 400;
  }
  .brand__legal::before, .brand__legal::after {
    content: ""; width: 92px; height: 2px; background: currentColor;
  }
  .brand__tagline {
    font-size: 13.5px; line-height: 20px; font-weight: 700;
    letter-spacing: 1.3px; margin-top: 6px; white-space: nowrap;
  }
  .contact { position: absolute; left: 0; right: 0; text-align: center; }
  .contact__name { top: 146px; font-size: 50px; line-height: 56px; font-weight: 700; }
  .contact__phone { top: 355px; font-size: 28px; line-height: 34px; letter-spacing: 1px; }
  .contact__email { top: 398px; font-size: 28px; line-height: 34px; }
</style>
</head>
<body>
  <section class="card card--front">
    <div class="brand brand--light">
      <p class="brand__name">MARLOW OUTINGS</p>
      <p class="brand__legal">PTY LTD</p>
      <p class="brand__tagline">in association with far reef cruises</p>
    </div>
    <div class="card__rule"></div>
    <div class="card__panel">
      <p class="contact contact__name">Pruntel</p>
      <p class="contact contact__phone">0468231594</p>
      <p class="contact contact__email">lpruntel7@tidewake.net</p>
    </div>
  </section>

  <section class="card card--back">
    <div class="card__photo" role="img" aria-label="Photo of the white charter boat moored at the marina"></div>
    <div class="card__rule"></div>
    <div class="card__panel">
      <div class="brand brand--dark">
        <p class="brand__name">MARLOW OUTINGS</p>
        <p class="brand__legal">PTY LTD</p>
        <p class="brand__tagline">in association with far reef cruises</p>
      </div>
    </div>
  </section>
</body>
</html>
```